New Business Card

We need to refresh our business cards. We designed these ourselves and we have no graphic design experience. We would like to find a new business card design that is professional and unique. We are an auto finance company. Feel free to play with the logo, but we would like to keep the eye very present on the card. Our corporate colors are green, grey, and white.
Green - RGB - 168,215,27; HEX - #AADD22
Grey - RGB - 196,196,196; HEX - #C4C4C4
Need to upload the vector file to finalize the project. The last logo was for a jpeg that didn't stretch well.
Industry/Entity Type
Financial Service
Contact Information for Business Card
Honestly don't know...I need your help!

```html
<!DOCTYPE html>
<html lang="en">
<head>
<meta charset="utf-8">
<title>Brightlane Capital – Business Card</title>
<link href="https://fonts.googleapis.com/css2?family=Oswald:wght@500&family=Work+Sans:wght@400;500;600&display=swap" rel="stylesheet">
<style>
  :root {
    --green: #aadd22;
    --grey: #c4c4c4;
    --white: #f4f4f4;
    --card: #1e1e1e;
    --card-edge: #262626;
    --backdrop: #2b2b2b;
  }
  * { box-sizing: border-box; margin: 0; padding: 0; }
  html, body {
    width: 1200px; height: 900px; overflow: hidden;
    background: var(--backdrop);
    font-family: "Work Sans", sans-serif;
  }
  .canvas {
    position: relative; width: 1200px; height: 900px;
  }
  .card {
    position: absolute; left: 290px; width: 620px; height: 354px;
    background: linear-gradient(135deg, var(--card-edge), var(--card) 60%);
    border-bottom: 6px solid var(--green);
    box-shadow: 0 10px 30px rgba(0,0,0,.45);
  }
  .card--front { top: 72px; }
  .card--back { top: 474px; }

  .brand {
    position: absolute; left: 0; right: 0; top: 150px;
    display: flex; align-items: center; justify-content: center; gap: 18px;
  }
  .brand__dot {
    width: 40px; height: 40px; border-radius: 50%; background: var(--green);
  }
  .brand__name {
    font-weight: 600; font-size: 40px; color: var(--green); letter-spacing: .5px;
  }

  .person {
    position: absolute; left: 40px; top: 128px; width: 210px; text-align: right;
  }
  .person__name {
    font-family: "Oswald", sans-serif; font-weight: 500; font-size: 36px;
    line-height: 1; color: var(--green); text-transform: uppercase; letter-spacing: -.5px;
  }
  .person__role {
    font-size: 16px; color: var(--white); margin-top: 6px; letter-spacing: .5px;
  }
  .divider {
    position: absolute; left: 272px; top: 120px; width: 2px; height: 78px; background: var(--green);
  }
  .contacts {
    position: absolute; left: 294px; top: 118px; list-style: none;
  }
  .contacts li {
    display: flex; align-items: center; gap: 10px;
    font-size: 17px; color: var(--white); line-height: 21px; letter-spacing: .4px;
  }
  .contacts svg { width: 12px; height: 12px; flex: none; }
  .contacts .accent { color: var(--green); }
  .address {
    position: absolute; left: 92px; bottom: 38px;
    font-size: 17px; color: var(--white); letter-spacing: .8px;
  }
</style>
</head>
<body>
<main class="canvas">
  <section class="card card--front">
    <div class="brand">
      <span class="brand__dot"></span>
      <span class="brand__name">Brightlane Capital</span>
    </div>
  </section>

  <section class="card card--back">
    <div class="person">
      <p class="person__name">Daniel Reyes</p>
      <p class="person__role">Director</p>
    </div>
    <span class="divider"></span>
    <ul class="contacts">
      <li>
        <svg viewBox="0 0 12 12"><path d="M3 1l2 2.5-1.2 1.2a7 7 0 0 0 3.5 3.5L8.5 7 11 9l-1.5 2C5 11 1 7 1 2.5z" fill="none" stroke="#aadd22" stroke-width="1.1"/></svg>
        (555)210-3800
      </li>
      <li>
        <svg viewBox="0 0 12 12"><rect x="3" y="1" width="6" height="10" rx="1" fill="none" stroke="#aadd22" stroke-width="1.1"/><circle cx="6" cy="9" r=".7" fill="#aadd22"/></svg>
        (555)418-7732
      </li>
      <li>
        <svg viewBox="0 0 12 12"><rect x="1" y="2.5" width="10" height="7" fill="none" stroke="#aadd22" stroke-width="1.1"/><path d="M1 2.5l5 4 5-4" fill="none" stroke="#aadd22" stroke-width="1.1"/></svg>
        dan@brightlanecapital.com
      </li>
      <li>
        <svg viewBox="0 0 12 12"><circle cx="6" cy="6" r="5" fill="none" stroke="#aadd22" stroke-width="1.1"/><path d="M1 6h10M6 1c-2.5 3-2.5 7 0 10M6 1c2.5 3 2.5 7 0 10" fill="none" stroke="#aadd22" stroke-width="1"/></svg>
        <span>www.<span class="accent">brightlanecapital</span>.com</span>
      </li>
    </ul>
    <p class="address">42 Meadow Lane, Lakeview, CA 90000</p>
  </section>
</main>
</body>
</html>
```